Logo für eine Distribution/Handelsunternehmung
Zielgruppe
Wir vertrieben Produkte aus der Audio-, Vieo- und Medientechnik. Die Produkte der Distribution sind ausschließlich für den professionellen Handel bestimmt. Die Produkte des Handelsunternehmens sind für professionelle Endanwender, Firmen und Institutionen bestimmt.
Aufgabenstellung
Bei dem Logodesign bin ich nicht festgelegt. Das Logo soll frisch und modern wirken, aber nicht zu verspielt oder unseriös. Das neue Unternehmen soll dadurch zwr präsent aber nicht aufdringlich wirken. Das Logo soll sowohl im Web wie auch im Print gut zur Geltung kommen.

```html
<!DOCTYPE html>
<html lang="de">
<head>
<meta charset="utf-8">
<title>Tonvara – Geschäftsausstattung</title>
<link href="https://fonts.googleapis.com/css2?family=Open+Sans:wght@400;600;700&display=swap" rel="stylesheet">
<style>
  :root {
    --bg: #efefed;
    --paper: #ffffff;
    --ink: #2b2b2b;
    --grey: #3d3d3d;
    --muted: #6a6a6a;
    --red: #9b1b20;
    --card-dark: #1e1e1e;
    --font: "Open Sans", Arial, sans-serif;
  }
  * { box-sizing: border-box; margin: 0; padding: 0; }
  html, body { width: 1200px; height: 744px; overflow: hidden; }
  body { background: var(--bg); font-family: var(--font); color: var(--ink); position: relative; }

  .brand { position: absolute; display: flex; align-items: center; }
  .brand-dot { border-radius: 50%; background: var(--red); flex: none; }
  .brand-name { font-family: var(--font); font-weight: 600; color: var(--grey); line-height: 1; letter-spacing: -0.01em; }
  .brand-tagline { position: absolute; font-weight: 600; color: var(--grey); letter-spacing: 0.08em; white-space: nowrap; text-transform: uppercase; }

  /* primary logo */
  .logo-main { left: 76px; top: 130px; }
  .logo-main .brand-dot { width: 62px; height: 62px; margin-right: 14px; }
  .logo-main .brand-name { font-size: 64px; }
  .logo-main-tagline { left: 155px; top: 183px; font-size: 7px; }

  /* business card front */
  .card { position: absolute; width: 145px; height: 96px; overflow: hidden; }
  .card-front { left: 326px; top: 305px; background: var(--card-dark); }
  .card-front .brand-name { position: absolute; left: 0; right: 0; top: 39px; text-align: center; color: #fff; font-size: 16px; }
  .card-front .brand-tagline { left: 0; right: 0; top: 58px; text-align: center; color: #d8d8d8; font-size: 2.6px; }

  /* business card back */
  .card-back { left: 326px; top: 435px; background: var(--paper); }
  .bar { position: absolute; }
  .bar-red { background: var(--red); }
  .bar-dark { background: var(--grey); }
  .card-back .bar-red { left: 7px; top: 0; width: 6px; height: 30px; }
  .card-back .bar-dark { left: 7px; top: 79px; width: 6px; height: 17px; }
  .card-logo { right: 7px; top: 8px; }
  .card-logo .brand-dot { width: 11px; height: 11px; margin-right: 3px; }
  .card-logo .brand-name { font-size: 13px; }
  .card-logo-tagline { right: 7px; top: 22px; font-size: 1.6px; }
  .person-name { position: absolute; left: 7px; top: 33px; font-size: 4px; font-weight: 700; color: var(--red); }
  .person-role { position: absolute; left: 7px; top: 38px; font-size: 3.3px; color: var(--muted); }
  .contact-list { position: absolute; left: 8px; top: 51px; list-style: none; font-size: 3.2px; line-height: 4.3px; }
  .contact-list li { display: flex; align-items: center; gap: 2px; }
  .contact-list svg { width: 3px; height: 3px; fill: var(--red); }
  .web-list { position: absolute; left: 8px; top: 68px; font-size: 3.2px; line-height: 4.3px; }
  .card-address { position: absolute; right: 7px; top: 83px; text-align: right; font-size: 3.2px; line-height: 4.3px; }
  .card-address strong { color: var(--red); font-weight: 700; }

  /* letterhead */
  .letterhead { position: absolute; left: 521px; top: 162px; width: 260px; height: 368px; background: var(--paper); box-shadow: 0 2px 6px rgba(0,0,0,0.08); overflow: hidden; }
  .letterhead-rule { position: absolute; left: 0; top: 24px; width: 146px; height: 1px; background: var(--ink); }
  .letterhead-logo { left: 152px; top: 10px; }
  .letterhead-logo .brand-dot { width: 14px; height: 14px; margin-right: 3px; }
  .letterhead-logo .brand-name { font-size: 15px; }
  .letterhead-logo-tagline { left: 170px; top: 26px; font-size: 1.6px; }
  .letterhead-rule-end { position: absolute; left: 254px; top: 24px; width: 6px; height: 1px; background: var(--red); }

  .sender-line { position: absolute; left: 30px; top: 74px; font-size: 2.6px; color: var(--muted); }
  .sender-line strong { color: var(--ink); }
  .recipient { position: absolute; left: 30px; top: 90px; font-size: 4.4px; line-height: 5.4px; }
  .letter-date { position: absolute; right: 30px; top: 121px; font-size: 4.6px; }
  .letter-subject { position: absolute; left: 30px; top: 142px; font-size: 4.6px; font-weight: 700; }
  .letter-body { position: absolute; left: 30px; top: 158px; width: 182px; font-size: 4.6px; line-height: 5.85px; }
  .letter-body p { margin-bottom: 5.8px; }
  .letter-closing { position: absolute; left: 30px; top: 251px; font-size: 4.6px; }
  .signature { position: absolute; left: 29px; top: 259px; width: 66px; height: 10px; background: linear-gradient(90deg, rgba(43,43,43,0.16), rgba(43,43,43,0.05)); border-radius: 2px; }

  .letterhead .footer-red { left: 0; top: 354px; width: 25px; height: 5px; }
  .letterhead .footer-dark { left: 235px; top: 354px; width: 25px; height: 5px; }
  .footer-col { position: absolute; top: 352px; font-size: 2.2px; line-height: 3px; color: var(--ink); white-space: nowrap; }
  .footer-col strong { color: var(--red); font-weight: 700; }
  .footer-col svg { width: 2px; height: 2px; fill: var(--red); vertical-align: middle; margin-right: 1px; }
</style>
</head>
<body>

  <!-- primary logo lockup -->
  <div class="brand logo-main">
    <span class="brand-dot"></span>
    <span class="brand-name">Tonvara</span>
  </div>
  <div class="brand-tagline logo-main-tagline">AV Solutions for Professionals</div>

  <!-- business card, front -->
  <section class="card card-front">
    <div class="brand-name">Tonvara</div>
    <div class="brand-tagline">AV Solutions for Professionals</div>
  </section>

  <!-- business card, back -->
  <section class="card card-back">
    <span class="bar bar-red"></span>
    <span class="bar bar-dark"></span>
    <div class="brand card-logo">
      <span class="brand-dot"></span>
      <span class="brand-name">Tonvara</span>
    </div>
    <div class="brand-tagline card-logo-tagline">AV Solutions for Professionals</div>
    <div class="person-name">Max Mustermann</div>
    <div class="person-role">Geschäftsführer</div>
    <ul class="contact-list">
      <li><svg viewBox="0 0 10 10"><path d="M2 0h2l1 3-1.5 1a6 6 0 0 0 2.5 2.5L7 5l3 1v2a2 2 0 0 1-2 2A8 8 0 0 1 0 2a2 2 0 0 1 2-2z"/></svg>+49 (0) 12 123 456 7</li>
      <li><svg viewBox="0 0 10 10"><rect x="1" y="3" width="8" height="7"/><rect x="3" y="0" width="4" height="3"/></svg>+49 (0) 12 123 456 8</li>
      <li><svg viewBox="0 0 10 10"><path d="M2 0h6v10H2zM3 1v7h4V1z"/></svg>+49 (0) 169 123 456 789</li>
    </ul>
    <div class="web-list">info@tonvara.de<br>www.tonvara.de</div>
    <div class="card-address"><strong>Tonvara</strong> AV-Solutions<br>Musterstr. 1 | D - 12345 Musterstadt</div>
  </section>

  <!-- letterhead -->
  <article class="letterhead">
    <span class="letterhead-rule"></span>
    <div class="brand letterhead-logo">
      <span class="brand-dot"></span>
      <span class="brand-name">Tonvara</span>
    </div>
    <div class="brand-tagline letterhead-logo-tagline">AV Solutions for Professionals</div>
    <span class="letterhead-rule-end"></span>

    <div class="sender-line"><strong>Tonvara</strong> AV-Solutions | Musterstr. 1 | D-12345 Musterstadt</div>
    <address class="recipient" style="font-style:normal">Herrn<br>Max Mustermann<br>Musterstraße 1<br>12345 Musterstadt</address>
    <div class="letter-date">Musterstadt, 23.11.2015</div>
    <div class="letter-subject">Betreff: Lorem Ipsum</div>
    <div class="letter-body">
      <p>Sehr geehrte Damen und Herren,</p>
      <p>Lorem ipsum dolor sit amet, consetetur sadipscing elitr, sed diam nonumy eirmod tempor invidunt ut labore et dolore magna aliquyam erat, sed diam voluptua. At vero eos et accusam et justo duo dolores et ea rebum. Stet clita kasd gubergren, no sea takimata sanctus est Lorem ipsum dolor sit amet. Lorem ipsum dolor sit amet, consetetur sadipscing elitr, sed diam nonumy eirmod tempor</p>
      <p>Duis autem vel eum iriure dolor in hendrerit in vulputate velit esse molestie consequat, vel illum dolore eu feugiat nulla facilisis at vero eros et accumsan et iusto odio dignissim qui blandit praesent luptatum zzril delenit augue duis dolore te feugait nulla facilisi. Lorem ipsum dolor sit amet.</p>
    </div>
    <div class="letter-closing">Mit freundlichen Grüßen</div>
    <div class="signature" role="img" aria-label="Handschriftliche Unterschrift von Max Mustermann"></div>

    <span class="bar bar-red footer-red"></span>
    <div class="footer-col" style="left:30px"><strong>Tonvara</strong> AV-Solutions<br>Musterstr. 1<br>D - 12345 Musterstadt</div>
    <div class="footer-col" style="left:66px"><strong>Max Mustermann</strong><br>info@tonvara.de<br>www.tonvara.de</div>
    <div class="footer-col" style="left:97px">
      <svg viewBox="0 0 10 10"><circle cx="5" cy="5" r="5"/></svg>+49 (0) 12 123 456 7<br>
      <svg viewBox="0 0 10 10"><circle cx="5" cy="5" r="5"/></svg>+49 (0) 12 123 456 8<br>
      <svg viewBox="0 0 10 10"><circle cx="5" cy="5" r="5"/></svg>+49 (0) 169 123 456 789
    </div>
    <div class="footer-col" style="left:138px">Kreisbank Musterstadt<br>IBAN DE12345600001234567890<br>BIC KRSBDEFFXXX</div>
    <div class="footer-col" style="left:187px">Amtsgericht Musterstadt<br>HRB0000<br>USt-IdNr.: DE000000000</div>
    <span class="bar bar-dark footer-dark"></span>
  </article>

</body>
</html>
```